Business Card Design

Sports massage therapist
Would like to convey a simple message.
graphic of human anatomy/muscular system
colours: orange with white/and or grey
glossey

Business

Fiona Tarrant
Soft Tissue Therapist
Sports and Remedial Massage
07914 562038
tarrant.fiona@pelmora.co.uk

```html
<!DOCTYPE html>
<html lang="en">
<head>
<meta charset="utf-8">
<title>Sports and Remedial Massage – Business Card</title>
<link href="https://fonts.googleapis.com/css2?family=Sorts+Mill+Goudy&family=Roboto:wght@400&display=swap" rel="stylesheet">
<style>
  :root {
    --backdrop: #e9e7e4;
    --orange-deep: #e0651a;
    --orange: #f0852a;
    --orange-light: #f7a45a;
    --white: #ffffff;
    --paper: #f4f4f4;
    --grey: #a9a9a9;
    --ink: #1d1d1d;
  }
  html, body {
    margin: 0;
    padding: 0;
    width: 1200px;
    height: 892px;
    overflow: hidden;
    background: var(--backdrop);
  }
  .canvas {
    position: relative;
    width: 1200px;
    height: 892px;
  }
  .business-card {
    position: absolute;
    left: 100px;
    top: 156px;
    width: 1000px;
    height: 580px;
    border-radius: 34px;
    overflow: hidden;
    background: linear-gradient(160deg, var(--white) 0%, var(--paper) 100%);
    box-shadow: 0 14px 36px rgba(0,0,0,0.22);
  }
  .card-art {
    position: absolute;
    inset: 0;
    width: 1000px;
    height: 580px;
  }
  .athlete-mark {
    position: absolute;
    left: 510px;
    top: 30px;
    width: 190px;
    height: 180px;
  }
  .service-title {
    position: absolute;
    left: 36px;
    top: 312px;
    margin: 0;
    font-family: "Sorts Mill Goudy", "Goudy Old Style", serif;
    font-weight: 400;
    font-size: 50px;
    line-height: 64px;
    color: var(--white);
    letter-spacing: 0.5px;
  }
  .service-title .title-second {
    display: block;
    padding-left: 72px;
  }
  .therapist {
    position: absolute;
    left: 460px;
    top: 440px;
  }
  .therapist-name {
    margin: 0;
    font-family: "Sorts Mill Goudy", "Goudy Old Style", serif;
    font-weight: 400;
    font-size: 46px;
    line-height: 52px;
    color: var(--orange);
    white-space: nowrap;
  }
  .therapist-role {
    margin: 4px 0 0 0;
    font-family: "Roboto", Arial, sans-serif;
    font-size: 25px;
    color: var(--ink);
    white-space: nowrap;
  }
  .contact {
    position: absolute;
    right: 40px;
    top: 290px;
    margin: 0;
    padding: 0;
    list-style: none;
    font-family: "Roboto", Arial, sans-serif;
    color: var(--ink);
  }
  .contact-item {
    display: flex;
    justify-content: flex-end;
    align-items: center;
    gap: 14px;
    height: 44px;
    white-space: nowrap;
  }
  .contact-phone { font-size: 27px; }
  .contact-email { font-size: 24px; }
  .contact-icon {
    width: 22px;
    height: 22px;
    background: var(--orange);
    border-radius: 2px;
    display: flex;
    align-items: center;
    justify-content: center;
  }
</style>
</head>
<body>
<main class="canvas">
  <article class="business-card">
    <svg class="card-art" viewBox="0 0 1000 580" aria-hidden="true">
      <defs>
        <linearGradient id="orangeGloss" x1="0" y1="1" x2="0.9" y2="0">
          <stop offset="0" stop-color="#e0651a"/>
          <stop offset="0.55" stop-color="#f0852a"/>
          <stop offset="1" stop-color="#f59a48"/>
        </linearGradient>
        <linearGradient id="shine" x1="0" y1="0" x2="0" y2="1">
          <stop offset="0" stop-color="#ffffff" stop-opacity="0.28"/>
          <stop offset="0.5" stop-color="#ffffff" stop-opacity="0.05"/>
          <stop offset="1" stop-color="#ffffff" stop-opacity="0"/>
        </linearGradient>
      </defs>
      <path class="grey-band" d="M890,0 C830,180 730,285 585,355 C445,425 320,465 272,580"
            fill="none" stroke="#a9a9a9" stroke-width="16"/>
      <path class="orange-field" d="M0,0 H860 C800,170 700,270 560,340 C420,410 290,450 240,580 H0 Z"
            fill="url(#orangeGloss)"/>
      <path class="gloss" d="M0,0 H860 C800,170 700,270 560,340 C420,410 290,450 240,580 H0 Z"
            fill="url(#shine)"/>
    </svg>

    <svg class="athlete-mark" role="img" aria-label="White running athlete figure symbol" viewBox="0 0 190 180">
      <rect x="0" y="0" width="190" height="180" rx="36" fill="#f49a4c"/>
    </svg>

    <h1 class="service-title">Sports and Remedial<span class="title-second">Massage</span></h1>

    <div class="therapist">
      <p class="therapist-name">Fiona Tarrant</p>
      <p class="therapist-role">Soft Tissue Therapist</p>
    </div>

    <ul class="contact">
      <li class="contact-item contact-phone">
        <span>07914 562038</span>
        <span class="contact-icon">
          <svg width="14" height="14" viewBox="0 0 14 14" aria-hidden="true">
            <path d="M3,1 L5,1 L6,4 L4.5,5 C5.3,7 6.8,8.6 9,9.5 L10,8 L13,9 L13,11 C13,12 12,13 11,13 C5.5,13 1,8.5 1,3 C1,2 2,1 3,1 Z" fill="#ffffff"/>
          </svg>
        </span>
      </li>
      <li class="contact-item contact-email">
        <span>tarrant.fiona@pelmora.co.uk</span>
        <span class="contact-icon">
          <svg width="14" height="12" viewBox="0 0 14 12" aria-hidden="true">
            <rect x="1" y="1.5" width="12" height="9" fill="none" stroke="#ffffff" stroke-width="1.4"/>
            <path d="M1,1.5 L7,7 L13,1.5" fill="none" stroke="#ffffff" stroke-width="1.4"/>
          </svg>
        </span>
      </li>
    </ul>
  </article>
</main>
</body>
</html>
```